Women's Online Clothing Boutique Needs Business Cards

I already have a logo that I would like to use. Some of the things that interest me is black business cards, foil embossed logo, glossy embossed logo, leopard print, no yellow font, rounded edges. I even like just a large logo on the front side with all of my information on the back side.

Contact Information for Business Card

https://silverheron.shopvenlo.com/
https://www.pagelink.net/thesilverheronboutique/
https://www.picfeed.net/thesilverheronboutique/
silverheronboutique@mailora.net

Requirements
Must have
• My Logo
Nice to have
• Leopard Print
Should not have
• No Yellow Font

```html
<!DOCTYPE html>
<html lang="en">
<head>
<meta charset="utf-8">
<title>The Silver Heron Boutique – Business Cards</title>
<link rel="stylesheet" href="https://fonts.googleapis.com/css2?family=Montserrat:wght@400;500&display=swap">
<style>
  :root {
    --backdrop: #3b3b3b;
    --card-black: #0d0d0d;
    --card-white: #ffffff;
    --logo-grey: #8a8a8a;
    --ink: #1a1a1a;
    --print-dark: #111111;
    --print-mid: #4a4a4a;
  }
  * { margin: 0; padding: 0; box-sizing: border-box; }
  html, body {
    width: 1200px;
    height: 900px;
    overflow: hidden;
    background: var(--backdrop);
    font-family: "Montserrat", sans-serif;
  }
  .canvas {
    position: relative;
    width: 1200px;
    height: 900px;
  }
  .card {
    position: absolute;
    left: 348px;
    width: 504px;
    height: 288px;
    border-radius: 22px;
    overflow: hidden;
  }
  .card--front {
    top: 140px;
    background: var(--card-black);
    display: flex;
    align-items: center;
    justify-content: center;
  }
  .brand-name {
    color: var(--logo-grey);
    font-weight: 400;
    font-size: 34px;
    letter-spacing: 0.5px;
    text-align: center;
    line-height: 1.25;
  }
  .card--back {
    top: 472px;
    background: var(--card-white);
  }
  .leopard-print {
    position: absolute;
    inset: 0;
    width: 100%;
    height: 100%;
  }
  .contact-list {
    position: absolute;
    list-style: none;
    font-size: 11.5px;
    font-weight: 400;
    color: var(--ink);
  }
  .contact-list li {
    display: flex;
    align-items: center;
    gap: 7px;
    line-height: 1.55;
  }
  .contact-list--web { left: 34px; top: 34px; }
  .contact-list--social { right: 30px; bottom: 30px; text-align: right; }
  .contact-list--social li { justify-content: flex-end; }
  .icon { width: 11px; height: 11px; flex: none; }
  .social-dot {
    width: 10px;
    height: 10px;
    border-radius: 50%;
    background: var(--ink);
    flex: none;
  }
</style>
</head>
<body>
<main class="canvas">
  <section class="card card--front" aria-label="Business card front">
    <p class="brand-name">The Silver Heron<br>Boutique</p>
  </section>

  <section class="card card--back" aria-label="Business card back">
    <svg class="leopard-print" viewBox="0 0 504 288" role="img" aria-label="Black and white leopard print pattern in diagonal bands">
      <defs>
        <linearGradient id="print-tone" x1="0" y1="0" x2="1" y2="1">
          <stop offset="0" stop-color="var(--print-dark)"/>
          <stop offset="0.5" stop-color="var(--print-mid)"/>
          <stop offset="1" stop-color="var(--print-dark)"/>
        </linearGradient>
      </defs>
      <path d="M150 0 H504 V150 C440 130 380 90 320 70 C260 55 200 40 150 0 Z" fill="url(#print-tone)"/>
      <path d="M0 95 C60 120 120 160 170 210 C200 240 230 265 250 288 H0 Z" fill="url(#print-tone)"/>
    </svg>

    <ul class="contact-list contact-list--web">
      <li>
        <svg class="icon" viewBox="0 0 12 12" aria-hidden="true">
          <circle cx="6" cy="6" r="5" fill="none" stroke="currentColor" stroke-width="1.2"/>
          <path d="M1 6 H11 M6 1 C3.5 4 3.5 8 6 11 M6 1 C8.5 4 8.5 8 6 11" fill="none" stroke="currentColor" stroke-width="0.9"/>
        </svg>
        silverheron.shopvenlo.com
      </li>
      <li>
        <svg class="icon" viewBox="0 0 12 12" aria-hidden="true">
          <rect x="0.6" y="2.2" width="10.8" height="7.6" rx="1" fill="currentColor"/>
          <path d="M1.2 2.8 L6 6.6 L10.8 2.8" fill="none" stroke="#ffffff" stroke-width="0.9"/>
        </svg>
        silverheronboutique@mailora.net
      </li>
    </ul>

    <ul class="contact-list contact-list--social">
      <li>thesilverheronboutique <span class="social-dot" aria-hidden="true"></span></li>
      <li>thesilverheronboutique <span class="social-dot" aria-hidden="true"></span></li>
    </ul>
  </section>
</main>
</body>
</html>
```